Clone http://www.velvorquillset.com/ (fully functioning WordPress website - not just design)

1) Clone or recreate http://www.velvorquillset.com/ in Wordpress with WooCommerece plugin
2) Connect to our Existing Quenz Account
3) Make site-wide text only changes that we provide you when site is complete.

We will provide all the graphics according to your size requirements.

Cash awarded to the closest copy of http://www.velvorquillset.com/

Target Market(s)

WordPress developer

Number of Pages Required

5+ page

Font styles to use
Sans Serif

Colors
abd037
cadf82
eaf2ce

Requirements
Must have
• Fully functioning website.

```html
<!DOCTYPE html>
<html lang="en">
<head>
<meta charset="utf-8">
<title>Oakline Consulting</title>
<link href="https://fonts.googleapis.com/css2?family=Open+Sans:wght@400;600;700&family=Roboto+Condensed:wght@400;700&display=swap" rel="stylesheet">
<style>
:root{
  --green:#abd037;
  --green-mid:#cadf82;
  --green-soft:#eaf2ce;
  --ink:#2b2b2b;
  --text:#555;
  --muted:#777;
  --line:#dcdcdc;
  --dark:#1d2026;
  --footer:#f1f1f1;
  --white:#fff;
  --teal:#2fb3bf;
}
*{box-sizing:border-box;margin:0;padding:0}
html,body{width:1200px;height:3186px;overflow:hidden}
body{position:relative;background:var(--white);font-family:"Open Sans",Arial,sans-serif;color:var(--text)}
.abs{position:absolute}
.head-font{font-family:"Roboto Condensed","Arial Narrow",sans-serif}

/* hero */
.hero{left:0;top:0;width:1200px;height:680px;background:linear-gradient(110deg,#2a2e33 0%,#4a5058 40%,#2c3036 70%,#1b1e22 100%)}
.hero::after{content:"";position:absolute;inset:0;background:rgba(0,0,0,.35)}
.hero > *{z-index:2}
.brand{left:100px;top:40px;display:flex;align-items:center;gap:14px;color:var(--white);font-family:"Roboto Condensed",sans-serif;font-weight:700;font-size:38px}
.brand .dot{width:54px;height:54px;border-radius:50%;background:var(--white)}
.topbar{right:100px;top:46px;display:flex;align-items:center;gap:12px;font-family:"Roboto Condensed",sans-serif;font-size:14px;color:var(--white)}
.flag{display:inline-block;width:24px;height:15px;background:#c8d0e0;margin:0 6px;vertical-align:middle}
.pill{height:30px;padding:0 20px;border-radius:15px;line-height:28px;font-size:14px;text-transform:uppercase}
.pill.register{background:var(--green);border:1px solid var(--green)}
.pill.login{border:2px solid var(--white);line-height:26px}
.nav{right:100px;top:103px;display:flex;gap:42px;font-family:"Roboto Condensed",sans-serif;font-size:16px;color:var(--white);text-transform:uppercase}
.slide-arrow{top:335px}
.hero-title{left:0;width:1200px;top:318px;text-align:center;color:var(--white);font-family:"Roboto Condensed",sans-serif;font-weight:700;font-size:42px}
.hero-sub{left:0;width:1200px;top:378px;text-align:center;color:var(--white);font-size:13px;line-height:24px}
.btn-green{left:510px;top:438px;width:180px;height:38px;border-radius:19px;background:var(--green);color:var(--white);font-family:"Roboto Condensed",sans-serif;font-size:16px;text-align:center;line-height:38px;text-transform:uppercase}

/* welcome */
.welcome-title{left:0;width:1200px;top:744px;text-align:center;font-family:"Roboto Condensed",sans-serif;font-size:40px;color:var(--ink)}
.welcome-title span{color:var(--green)}
.welcome-text{left:160px;width:880px;top:806px;text-align:center;font-size:11px;line-height:19px;color:var(--muted)}

/* feature cards */
.card{left:127px;width:941px;height:304px;border:1px solid var(--line);background:var(--white)}
.card .num{position:absolute;width:0;height:0;border-style:solid}
.card.left-num .num{left:-1px;top:-1px;border-width:86px 86px 0 0;border-color:var(--green) transparent transparent transparent}
.card.right-num .num{right:-1px;top:-1px;border-width:0 86px 86px 0;border-color:transparent var(--green) transparent transparent}
.card .digit{position:absolute;top:8px;color:var(--white);font-family:"Roboto Condensed",sans-serif;font-weight:700;font-size:36px}
.card.left-num .digit{left:12px}
.card.right-num .digit{right:12px}
.card h3{position:absolute;top:42px;width:540px;font-family:"Roboto Condensed",sans-serif;font-weight:400;font-size:26px;line-height:32px;color:var(--ink)}
.card p{position:absolute;top:118px;width:540px;font-size:11px;line-height:21px;color:var(--muted)}
.card .read{position:absolute;top:234px;width:98px;height:32px;border-radius:16px;background:var(--ink);color:var(--white);font-size:13px;text-align:center;line-height:32px}
.card.left-num h3,.card.left-num p,.card.left-num .read{left:70px}
.card.right-num h3,.card.right-num p,.card.right-num .read{left:340px}
.card .art{position:absolute;top:36px;width:230px;height:230px;border-radius:50%;outline:2px dotted #ccc;outline-offset:8px}
.card.left-num .art{right:70px}
.card.right-num .art{left:62px}

/* testimonials */
.testimonials{left:0;top:2001px;width:1200px;height:342px;background:linear-gradient(135deg,#1b1e23 0%,#3a3f47 45%,#23272d 100%)}
.testimonials h2{position:absolute;left:0;width:1200px;top:64px;text-align:center;color:var(--white);font-family:"Roboto Condensed",sans-serif;font-weight:400;font-size:32px}
.testimonials .quote{position:absolute;left:205px;width:790px;top:124px;text-align:center;color:var(--white);font-size:12px;line-height:21px}
.testimonials .qmark{position:absolute;left:210px;top:112px;color:var(--white);font-size:34px;font-style:italic;font-family:Georgia,serif}
.testimonials .who{position:absolute;left:0;width:1200px;top:218px;text-align:center;color:var(--white);font-style:italic;font-size:20px;font-family:"Roboto Condensed",sans-serif}
.testimonials .who small{font-size:14px}
.dots{position:absolute;left:552px;top:264px;display:flex;gap:6px}
.dots i{display:block;width:30px;height:3px;background:#777}
.dots i.on{background:var(--white)}

/* services */
.services-title{left:0;width:1200px;top:2410px;text-align:center;font-family:"Roboto Condensed",sans-serif;font-size:34px;color:var(--ink)}
.service{top:2513px;width:240px;text-align:center}
.service .icon{width:106px;height:106px;border-radius:50%;background:var(--green);margin:0 auto;display:flex;align-items:center;justify-content:center}
.service h4{margin-top:26px;font-family:"Roboto Condensed",sans-serif;font-weight:400;font-size:15px;color:var(--ink);text-transform:uppercase}
.service p{margin-top:6px;font-size:11px;line-height:19px;color:var(--muted)}
.service .more{margin-top:10px}

/* footer */
.footer{left:0;top:2836px;width:1200px;height:297px;background:var(--footer)}
.footer-brand{left:106px;top:2890px;width:140px;text-align:center}
.footer-brand .name{display:flex;align-items:center;justify-content:center;gap:10px;font-family:"Roboto Condensed",sans-serif;font-weight:700;font-size:30px;color:var(--green)}
.footer-brand .name i{display:block;width:22px;height:22px;border-radius:50%;background:var(--green)}
.socials{display:flex;gap:6px;justify-content:center;margin-top:120px}
.socials i{display:block;width:20px;height:20px;border-radius:50%;border:1.5px solid #555}
.fcol h5{font-family:"Roboto Condensed",sans-serif;font-weight:400;font-size:18px;color:var(--ink);text-transform:uppercase;margin-bottom:22px}
.contact{left:346px;top:2884px;width:240px;font-size:13px;line-height:20px;color:var(--text)}
.contact .row{display:flex;gap:14px;margin-bottom:14px}
.newsletter{left:622px;top:2884px;width:300px;font-size:12px;line-height:20px;color:var(--text)}
.newsletter .field{margin-top:14px;width:300px;height:42px;background:var(--white);border:1px solid #e2e2e2;font-size:12px;line-height:40px;padding-left:12px}
.newsletter .submit{margin-top:14px;width:124px;height:38px;background:var(--green);color:var(--white);font-family:"Roboto Condensed",sans-serif;font-weight:700;font-size:16px;text-align:center;line-height:38px;text-transform:uppercase}
.links{left:1003px;top:2884px;width:120px;font-size:12px;color:var(--text)}
.links li{list-style:none;line-height:21px;padding-left:18px;position:relative}
.links li::before{content:"";position:absolute;left:2px;top:7px;border-left:6px solid #444;border-top:4px solid transparent;border-bottom:4px solid transparent}
.copyright{left:0;top:3133px;width:1200px;height:53px;background:var(--white);text-align:center;line-height:53px;font-size:11px;color:var(--text)}
</style>
</head>
<body>

<header class="abs hero" role="img" aria-label="Photo of a consultant working at a laptop in a bright office">
  <div class="abs brand"><span class="dot"></span>Oakline</div>
  <div class="abs topbar"><span>LANGUAGE<span class="flag"></span>&#8964;</span><span class="pill register">Register</span><span class="pill login">Log-in</span></div>
  <nav class="abs nav"><span>Home</span><span>About us</span><span>Products</span><span>Services</span><span>News</span><span>Contact</span></nav>
  <svg class="abs slide-arrow" style="left:44px" width="34" height="60" viewBox="0 0 34 60"><path d="M30 2 4 30l26 28" fill="none" stroke="#fff" stroke-width="2"/></svg>
  <svg class="abs slide-arrow" style="left:1122px" width="34" height="60" viewBox="0 0 34 60"><path d="M4 2l26 28L4 58" fill="none" stroke="#fff" stroke-width="2"/></svg>
  <h1 class="abs hero-title">OAKLINE CONSULTING</h1>
  <p class="abs hero-sub">Nemo enim ipsam voluptatem quia voluptas sit aspernatur aut odit aut fugit,<br>sed quia consequuntur magni dolores eos qui ratione voluptatem</p>
  <div class="abs btn-green">Get started today</div>
</header>

<h2 class="abs welcome-title">WELCOME TO <span>OAKLINE</span></h2>
<p class="abs welcome-text">Sed ut perspiciatis unde omnis iste natus error sit voluptatem accusantium doloremque laudantium, totam rem aperiam, eaque ipsa quae ab illo inventore veritatis et quasi architecto beatae vitae dicta sunt explicabo. Nemo enim ipsam voluptatem quia voluptas sit aspernatur aut odit aut fugit, sed quia consequuntur magni dolores eos qui ratione voluptatem sequi nesciunt. Neque porro quisquam est, qui dolorem ipsum quia dolor sit amet, consectetur, adipisci velit, sed quia non numquam eius modi tempora incidunt ut labore et dolore magnam aliquam quaerat voluptatem. Ut enim ad minima veniam, quis nostrum</p>

<section class="abs card left-num" style="top:939px">
  <span class="num"></span><span class="digit">1</span>
  <h3>Nemo enim ipsam voluptatem quia voluptas sit aspernatur aut odit aut fugit,</h3>
  <p>Sed ut perspiciatis unde omnis iste natus error sit voluptatem accusantium doloremque laudantium, totam rem aperiam, eaque ipsa quae ab illo inventore veritatis et quasi architecto beatae vitae dicta sunt explicabo. Nemo enim ipsam voluptatem quia voluptas sit aspernatur aut odit aut fugit, sed quia consequuntur magni dolores eos qui ratione voluptatem sequi nesciunt. Neque porro quisquam est, qui dolorem ipsum quia dolor sit amet, consectetur, adipisci velit, sed quia</p>
  <span class="read">Read More</span>
  <div class="art" style="background:var(--green)" role="img" aria-label="Illustration of a monitor with analytics charts and a magnifier"></div>
</section>

<section class="abs card right-num" style="top:1264px">
  <span class="num"></span><span class="digit">2</span>
  <h3>Nemo enim ipsam voluptatem quia voluptas sit aspernatur aut odit aut fugit,</h3>
  <p>Sed ut perspiciatis unde omnis iste natus error sit voluptatem accusantium doloremque laudantium, totam rem aperiam, eaque ipsa quae ab illo inventore veritatis et quasi architecto beatae vitae dicta sunt explicabo. Nemo enim ipsam voluptatem quia voluptas sit aspernatur aut odit aut fugit, sed quia consequuntur magni dolores eos qui ratione voluptatem sequi nesciunt. Neque porro quisquam est, qui dolorem ipsum quia dolor sit amet, consectetur, adipisci velit, sed quia</p>
  <span class="read">Read More</span>
  <div class="art" style="background:var(--teal)" role="img" aria-label="Illustration of a web page, light bulb, pen and keyboard"></div>
</section>

<section class="abs card left-num" style="top:1597px">
  <span class="num"></span><span class="digit">3</span>
  <h3>Nemo enim ipsam voluptatem quia voluptas sit aspernatur aut odit aut fugit,</h3>
  <p>Sed ut perspiciatis unde omnis iste natus error sit voluptatem accusantium doloremque laudantium, totam rem aperiam, eaque ipsa quae ab illo inventore veritatis et quasi architecto beatae vitae dicta sunt explicabo. Nemo enim ipsam voluptatem quia voluptas sit aspernatur aut odit aut fugit, sed quia consequuntur magni dolores eos qui ratione voluptatem sequi nesciunt. Neque porro quisquam est, qui dolorem ipsum quia dolor sit amet, consectetur, adipisci velit, sed quia</p>
  <span class="read">Read More</span>
  <div class="art" style="background:#8cc152" role="img" aria-label="Illustration of a dashboard screen with charts and a stopwatch"></div>
</section>

<section class="abs testimonials" role="img" aria-label="Dark photo of a glass office building">
  <h2>TESTIMONIALS</h2>
  <span class="qmark">&ldquo;</span>
  <p class="quote">Lorem ipsum dolor sit amet, consectetur adipiscing elit, sed do eiusmod tempor incididunt ut labore et dolore magna aliqua. Ut enim ad minim veniam, quis nostrud exercitation ullamco laboris nisi ut aliquip ex ea commodo consequat. Duis aute irure dolor in reprehenderit in voluptate velit esse cillum dolore eu fugiat nulla Sed ut perspiciatis unde omnis iste natus error sit voluptatem accusantium doloremque laudantium, totam rem aperiam, eaque ipsa quae ab illo inventore veritatis et quasi architecto beatae vitae</p>
  <p class="who">Elias Varn <small>- Oakline</small></p>
  <div class="dots"><i class="on"></i><i></i><i></i></div>
</section>

<h2 class="abs services-title">OUR SERVICES</h2>

<div class="abs service" style="left:86px">
  <div class="icon"><svg width="48" height="48" viewBox="0 0 48 48"><path d="M6 14h12a5 5 0 1 1 10 0h12v12a5 5 0 1 0 0 10v6H6z" fill="#fff"/></svg></div>
  <h4>Sed ut perspiciatis unde</h4>
  <p>Sed ut perspiciatis unde omnis iste natus error sit voluptatem accusantium doloque laudantium, totam rem dolores</p>
  <svg class="more" width="16" height="16" viewBox="0 0 16 16"><path d="M2 2l6 5 6-5M2 8l6 5 6-5" fill="none" stroke="#333" stroke-width="2"/></svg>
</div>
<div class="abs service" style="left:349px">
  <div class="icon"><svg width="50" height="44" viewBox="0 0 50 44"><path d="M4 2v38h44" fill="none" stroke="#fff" stroke-width="3"/><path d="M10 32l12-12 8 8 14-16" fill="none" stroke="#fff" stroke-width="3"/><path d="M38 10h8v8" fill="none" stroke="#fff" stroke-width="3"/></svg></div>
  <h4>Nemo enim ipsam</h4>
  <p>Sed ut perspiciatis unde omnis iste natus error sit voluptatem accusantium doloque laudantium, totam rem dolores</p>
  <svg class="more" width="16" height="16" viewBox="0 0 16 16"><path d="M2 2l6 5 6-5M2 8l6 5 6-5" fill="none" stroke="#333" stroke-width="2"/></svg>
</div>
<div class="abs service" style="left:615px">
  <div class="icon"><svg width="48" height="48" viewBox="0 0 48 48"><circle cx="24" cy="24" r="19" fill="none" stroke="#fff" stroke-width="6"/><circle cx="24" cy="24" r="8" fill="none" stroke="#fff" stroke-width="3"/><path d="M10 10l8 8M38 10l-8 8M10 38l8-8M38 38l-8-8" stroke="#abd037" stroke-width="4"/></svg></div>
  <h4>Sed ut perspiciatis unde</h4>
  <p>Sed ut perspiciatis unde omnis iste natus error sit voluptatem accusantium doloque laudantium, totam rem dolores</p>
  <svg class="more" width="16" height="16" viewBox="0 0 16 16"><path d="M2 2l6 5 6-5M2 8l6 5 6-5" fill="none" stroke="#333" stroke-width="2"/></svg>
</div>
<div class="abs service" style="left:872px">
  <div class="icon"><svg width="52" height="40" viewBox="0 0 52 40"><rect x="8" y="3" width="36" height="26" rx="2" fill="none" stroke="#fff" stroke-width="3"/><path d="M2 33h48l-3 4H5z" fill="#fff"/></svg></div>
  <h4>Nemo enim ipsam</h4>
  <p>Sed ut perspiciatis unde omnis iste natus error sit voluptatem accusantium doloque laudantium, totam rem dolores</p>
  <svg class="more" width="16" height="16" viewBox="0 0 16 16"><path d="M2 2l6 5 6-5M2 8l6 5 6-5" fill="none" stroke="#333" stroke-width="2"/></svg>
</div>

<footer class="abs footer"></footer>
<div class="abs footer-brand">
  <div class="name"><i></i>Oakline</div>
  <div class="socials"><i></i><i></i><i></i><i></i></div>
</div>
<div class="abs fcol contact">
  <h5>Contact us</h5>
  <div class="row"><svg width="14" height="18" viewBox="0 0 14 18"><path d="M7 1a6 6 0 0 1 6 6c0 4-6 10-6 10S1 11 1 7a6 6 0 0 1 6-6z" fill="#555"/><circle cx="7" cy="7" r="2" fill="#f1f1f1"/></svg><span>Oakline<br>Corven Row, Aldmere AX4 7QP</span></div>
  <div class="row"><svg width="14" height="14" viewBox="0 0 14 14"><path d="M3 1l3 3-2 2c1 2 2 3 4 4l2-2 3 3-2 2C6 13 1 8 1 3z" fill="#555"/></svg><span>Phone: (555) 014-2290</span></div>
  <div class="row"><svg width="14" height="12" viewBox="0 0 14 12"><rect x="0" y="1" width="14" height="10" fill="#555"/><path d="M0 1l7 6 7-6" fill="none" stroke="#f1f1f1"/></svg><span>info@oakline-mail.test</span></div>
</div>
<div class="abs fcol newsletter">
  <h5>Sign up for newsletter</h5>
  <p>Excepteur sint occaecat cupidatat non proident, sunt in culpa qui officia deserunt</p>
  <div class="field">Enter email</div>
  <div class="submit">Sign up</div>
</div>
<ul class="abs fcol links">
  <h5>Quick links</h5>
  <li>Home</li><li>About</li><li>Team</li><li>Our Services</li><li>Oakline</li><li>Blog</li><li>Contact Us</li>
</ul>
<div class="abs copyright">&copy;2017 Oakline, All Rights Reserved.</div>

</body>
</html>
```